Freelancer Information Security professional needs a business card

I need a simple, young, elegant business card. I'm a freelancer in the InfoSec area and want to be able to give my card to potential customers and new people I meet.

I'd like to have a clean, professional look but at same time not boring or corporate.

The only requirement is to have my "introduction" phrase which is:
"Half hacker, half mercenary."

I have added a card I have as a example, which I think it gives a good example of style I want.

Target Market(s)

Technology / Computers / Engineering

Industry/Entity Type

Information Technology

Contact Information for Business Card

Contact fields I want included:

(351) 93 708 16 52
tomas@vorelin.im
https://vorelin.im

Font styles to use
Sans Serif

Requirements
Nice to have
• Card doesn't need to have a doubled side, but it looks good / fits the design then please do include.
Should not have
• Outdated graphics or images; too much patterns/colors.

```html
<!DOCTYPE html>
<html lang="en">
<head>
<meta charset="utf-8">
<title>Tomas Vorelin — Business Card</title>
<link rel="stylesheet" href="https://fonts.googleapis.com/css2?family=Roboto+Condensed:wght@300;400;700&display=swap">
<style>
  :root {
    --blue: #0a9fe0;
    --green: #97c12c;
    --ink: #232323;
    --paper: #ffffff;
    --backdrop: #f2f2f2;
  }
  * { margin: 0; padding: 0; box-sizing: border-box; }
  html, body {
    width: 1200px;
    height: 857px;
    overflow: hidden;
    background: var(--backdrop);
    font-family: "Roboto Condensed", "Arial Narrow", sans-serif;
  }
  .card {
    position: absolute;
    left: 60px;
    top: 108px;
    width: 1080px;
    height: 640px;
    background: var(--paper);
    overflow: hidden;
  }
  .identity {
    position: absolute;
    left: 155px;
    top: 152px;
  }
  .name {
    font-weight: 700;
    font-size: 56px;
    line-height: 1;
    letter-spacing: 3px;
    text-transform: uppercase;
    color: var(--blue);
  }
  .name .surname { color: var(--green); }
  .tagline {
    margin-top: 14px;
    font-weight: 300;
    font-size: 32px;
    line-height: 1;
    text-transform: uppercase;
    color: var(--blue);
  }
  .contact-row {
    position: absolute;
    left: 0;
    height: 62px;
    width: 900px;
  }
  .contact-row .band {
    position: absolute;
    left: 0;
    top: 0;
    width: 300px;
    height: 62px;
    border-radius: 0 31px 31px 0;
  }
  .contact-row .badge {
    position: absolute;
    left: 260px;
    top: -9px;
    width: 80px;
    height: 80px;
    border-radius: 50%;
    border: 7px solid var(--paper);
    display: flex;
    align-items: center;
    justify-content: center;
  }
  .contact-row .badge svg { width: 40px; height: 40px; }
  .contact-row .value {
    position: absolute;
    left: 352px;
    top: 0;
    line-height: 62px;
    font-weight: 400;
    font-size: 33px;
    color: var(--ink);
    white-space: nowrap;
  }
  .row-phone { top: 300px; }
  .row-mail { top: 385px; }
  .row-web { top: 464px; }
  .is-green { background: var(--green); }
  .is-blue { background: var(--blue); }
  .edge-stripes {
    position: absolute;
    top: 0;
    right: 0;
    height: 100%;
    width: 54px;
  }
</style>
</head>
<body>
  <div class="card">
    <div class="identity">
      <h1 class="name">Tomas <span class="surname">Vorelin</span></h1>
      <p class="tagline">Half hacker, half mercenary.</p>
    </div>

    <div class="contact-row row-phone">
      <div class="band is-green"></div>
      <div class="badge is-green">
        <svg viewBox="0 0 40 40" fill="none" stroke="#232323" stroke-width="2.4">
          <rect x="10" y="3" width="20" height="34" rx="3"/>
          <line x1="10" y1="29" x2="30" y2="29"/>
          <circle cx="17" cy="33" r="0.8" fill="#232323"/>
          <circle cx="20" cy="33" r="0.8" fill="#232323"/>
          <circle cx="23" cy="33" r="0.8" fill="#232323"/>
        </svg>
      </div>
      <span class="value">(351) 93 708 16 52</span>
    </div>

    <div class="contact-row row-mail">
      <div class="band is-blue"></div>
      <div class="badge is-blue">
        <svg viewBox="0 0 40 40" fill="none" stroke="#232323" stroke-width="2.6" stroke-linejoin="round">
          <rect x="3" y="9" width="34" height="22" rx="2"/>
          <polyline points="3,10 20,23 37,10"/>
          <line x1="3" y1="30" x2="15" y2="19"/>
          <line x1="37" y1="30" x2="25" y2="19"/>
        </svg>
      </div>
      <span class="value">tomas@vorelin.im</span>
    </div>

    <div class="contact-row row-web">
      <div class="band is-green"></div>
      <div class="badge is-green">
        <svg viewBox="0 0 40 40" fill="none" stroke="#232323" stroke-width="2.2">
          <circle cx="20" cy="20" r="16"/>
          <ellipse cx="20" cy="20" rx="7" ry="16"/>
          <line x1="20" y1="4" x2="20" y2="36"/>
          <line x1="4" y1="20" x2="36" y2="20"/>
          <path d="M7 12 H33 M7 28 H33"/>
        </svg>
      </div>
      <span class="value">https://vorelin.im</span>
    </div>

    <svg class="edge-stripes" viewBox="0 0 54 640" preserveAspectRatio="none" aria-hidden="true">
      <rect x="0" y="0" width="10" height="640" fill="var(--blue)"/>
      <rect x="13" y="0" width="9" height="640" fill="var(--green)"/>
      <rect x="25" y="0" width="9" height="640" fill="var(--blue)"/>
      <rect x="37" y="0" width="17" height="640" fill="var(--green)"/>
    </svg>
  </div>
</body>
</html>
```